Business Card Design

I am in the progress of starting up my business.

Business Name - KT Surface Cleaning

Services that we offer
- Driveway Cleaning
- Foot Path Cleaning
- Pebble & Normal Cement
- Gutter Clean Out
- Removal of Moss & Mould
- Moss & Mould treatment is also available
- Entertainment & Courtyard Area's etc
- Gutter Guard Installation
- Full roof restoration, We Only Use Veltrano Products
- (veltrano application licence, Includes a full 10 year full warrenty )

New Business Card Information - I would like to get rid of "We cover all maitland & Newcastle regions" And Change it to Newcastle Region Hunter Valley Region Nelson Bay Region And the List on the back I would also like to change to OUR SERVICES Driveway & Foot Path Cleaning Treatment & Removal Of Moss & Mould Entertainment & Deck Area's Pebble Crete & cemented Area's Factory & Office Fronts House Exterior (Windows, Veranda's, Brick Work) Roof & Gutter Cleaning Roof Restoration - Veltrano, Korvin Roof Membrane 418 (Veltrano Application Licence, Includes Full 10 Year Warranty)

Industry/Entity Type

Business

Contact Information for Business Card

KT Surface Washing
Water Blasting And Roof Restorations
ABN # 47 219 806 153
Phone # 0417385926
Contact Reid For A Free Quote
Cover Maitland & Newcastle Region's

[Can you please send me an email when you would like me to send through picture as this page wont allow me to add pictures]

Thanks Reid

Requirements
Must have
• Main details on the front of the business card and a picture or two. on the back of the business I would like the list of services that my company provide on the back
Nice to have
• I was hoping that on the front of the business I could have all the company information and details and maybe a picture or two if able to. On the back of the card I would like the services I provide listed but also not over crowded at the same time..

```html
<!DOCTYPE html>
<html lang="en">
<head>
<meta charset="utf-8">
<title>KT Surface Cleaning – Business Card</title>
<link rel="stylesheet" href="https://fonts.googleapis.com/css2?family=Open+Sans:ital,wght@0,600;0,700;0,800;1,700&family=Ubuntu:wght@500&family=Kalam:wght@700&display=swap">
<style>
  :root {
    --bg: #e9e6e2;
    --brown: #8c5a25;
    --brown-dark: #6e4318;
    --brown-light: #a56f34;
    --orange: #f0801e;
    --white: #ffffff;
    --yellow: #f2e21a;
    --ink: #161616;
    --stone: #9a9a96;
    --brick: #b8654a;
    --roof: #c9ccc8;
  }
  * { box-sizing: border-box; margin: 0; padding: 0; }
  html, body { width: 1200px; height: 1200px; overflow: hidden; }
  body {
    background: var(--bg);
    font-family: "Open Sans", Arial, sans-serif;
    position: relative;
  }
  .card {
    position: absolute;
    left: 110px;
    width: 980px;
    height: 560px;
    overflow: hidden;
    background: var(--brown);
    box-shadow: 0 6px 18px rgba(0,0,0,.18);
  }
  .card-back { top: 30px; }
  .card-front { top: 610px; }
  .card svg.shapes { position: absolute; inset: 0; width: 100%; height: 100%; }

  /* back side */
  .services {
    position: absolute;
    left: 0; right: 0;
    top: 150px;
    text-align: center;
    color: var(--white);
    font-weight: 600;
    font-size: 21px;
    line-height: 1.55;
  }
  .services-title {
    font-size: 28px;
    font-weight: 700;
    margin-bottom: 6px;
    letter-spacing: .5px;
  }
  .services-warranty { color: var(--yellow); }

  /* front side */
  .brand-name {
    position: absolute;
    left: 60px; top: 26px;
    font-size: 62px;
    font-weight: 800;
    color: var(--white);
    letter-spacing: 1px;
    white-space: nowrap;
  }
  .brand-tagline {
    position: absolute;
    left: 40px; top: 112px;
    width: 900px;
    display: flex;
    align-items: center;
    gap: 14px;
    color: var(--white);
    font-style: italic;
    font-weight: 700;
    font-size: 24px;
    white-space: nowrap;
  }
  .brand-tagline::before,
  .brand-tagline::after {
    content: "";
    flex: 1;
    height: 3px;
    background: var(--white);
  }
  .contact-box {
    position: absolute;
    left: 390px; top: 200px;
    width: 545px; height: 300px;
    border: 4px solid var(--white);
    border-radius: 28px;
    background: linear-gradient(180deg, var(--brown-light), var(--brown-dark));
    color: var(--white);
    text-align: center;
    font-family: "Ubuntu", Arial, sans-serif;
    font-weight: 500;
    padding-top: 16px;
  }
  .contact-lead { font-size: 30px; }
  .contact-regions { font-size: 26px; line-height: 1.35; margin-top: 6px; }
  .contact-phone {
    display: flex;
    align-items: center;
    justify-content: center;
    gap: 22px;
    margin-top: 18px;
  }
  .contact-phone svg { width: 92px; height: 80px; }
  .phone-number {
    font-family: "Kalam", cursive;
    font-weight: 700;
    font-size: 58px;
    letter-spacing: 1px;
  }
  .abn {
    position: absolute;
    left: 28px; bottom: 22px;
    color: var(--ink);
    font-weight: 800;
    font-size: 26px;
  }
</style>
</head>
<body>

  <!-- Back: services -->
  <section class="card card-back">
    <svg class="shapes" viewBox="0 0 980 560" preserveAspectRatio="none">
      <defs>
        <linearGradient id="stone-fill" x1="0" y1="0" x2="1" y2="1">
          <stop offset="0" stop-color="#b3b2ad"/>
          <stop offset="1" stop-color="#7f7e79"/>
        </linearGradient>
        <linearGradient id="brick-fill" x1="0" y1="0" x2="1" y2="1">
          <stop offset="0" stop-color="#c47257"/>
          <stop offset="1" stop-color="#9e5640"/>
        </linearGradient>
      </defs>
      <path role="img" aria-label="Photo of an exposed aggregate pebble-crete surface" fill="url(#stone-fill)"
            d="M0,0 H980 V90 L0,140 Z"/>
      <path role="img" aria-label="Photo of cleaned red brick paving" fill="url(#brick-fill)"
            d="M0,420 L980,360 V560 H0 Z"/>
      <path fill="var(--brown)" d="M0,140 L980,90 V360 L0,420 Z"/>
      <path fill="var(--orange)" d="M0,132 L980,82 V94 L0,146 Z"/>
      <path fill="var(--orange)" d="M0,414 L980,354 V368 L0,428 Z"/>
    </svg>
    <div class="services">
      <p class="services-title">Services that we offer</p>
      <p>Driveway | Foot Path Cleaning Treatment | Removal Of Moss</p>
      <p>Mould Entertainment | Deck Area's Pebble Crete | cemented Area's Factory</p>
      <p>Office Fronts House Exterior (Windows, Veranda's, Brick Work) Roof</p>
      <p>Gutter Cleaning Roof Restoration - Veltrano, Korvin Roof Membrane 418</p>
      <p class="services-warranty">(Veltrano Application Licence, Includes Full 10 Year Warranty)</p>
    </div>
  </section>

  <!-- Front: contact details -->
  <section class="card card-front">
    <svg class="shapes" viewBox="0 0 980 560" preserveAspectRatio="none">
      <defs>
        <linearGradient id="roof-fill" x1="0" y1="0" x2="1" y2="1">
          <stop offset="0" stop-color="#5f7f4e"/>
          <stop offset=".4" stop-color="#b9bcb8"/>
          <stop offset="1" stop-color="#d9dbd7"/>
        </linearGradient>
      </defs>
      <path fill="var(--orange)" d="M0,172 C260,120 540,140 980,222 V250 C540,168 260,150 0,196 Z"/>
      <path role="img" aria-label="Photo of a worker pressure cleaning a tiled roof"
            fill="url(#roof-fill)"
            d="M0,196 C260,150 540,168 980,250 V560 H0 Z"/>
      <path fill="var(--orange)" d="M500,560 C680,470 840,420 980,400 V560 Z"/>
    </svg>

    <h1 class="brand-name">KT SURFACE CLEANING</h1>
    <p class="brand-tagline">Washing Water Blasting And Roof Restorations</p>

    <div class="contact-box">
      <p class="contact-lead">Contact Reid For A Free Quote</p>
      <p class="contact-regions">Newcastle Region Hunter Valley Region<br>Nelson Bay Region</p>
      <div class="contact-phone">
        <svg viewBox="0 0 92 80" aria-hidden="true">
          <path fill="var(--white)" d="M6,22 C6,10 20,4 46,4 C72,4 86,10 86,22 V30 H66 V20 H26 V30 H6 Z"/>
          <path fill="var(--white)" d="M28,32 H64 L80,62 V76 H12 V62 Z"/>
          <circle cx="46" cy="56" r="11" fill="var(--brown-dark)"/>
          <circle cx="46" cy="56" r="4" fill="var(--white)"/>
        </svg>
        <span class="phone-number"># 0417385926</span>
      </div>
    </div>

    <p class="abn">ABN# 47 219 806 153</p>
  </section>

</body>
</html>
```